Window Dressing of css files in existing web based application

We have a pretty large application which depends mostly on couple of css file that could be seriously improved. The application generates the pages so this job really consists of updating almost only the css file and possibly defined new css classes and affect them to existing objects, table, div, form etc....

Modifying the html pages structure nor an option OR the goal. The goal truly is to change only css files and possibly classes attribution to existing pages making any change in the css reflects properly in all pages (since they share the same css!!)

Target Market(s)

Veterinary

Coding

Coded - Design and coding required

Number of Pages Required

1 page

Requirements
Must have
• CSS knowledge
Nice to have
• Javascript

```html
<!DOCTYPE html>
<html lang="en">
<head>
<meta charset="utf-8">
<title>The Veterinary Demo Clinic #2588 – Home</title>
<link href="https://fonts.googleapis.com/css2?family=Arimo:wght@400;700&family=Source+Sans+3:wght@400;600&display=swap" rel="stylesheet">
<style>
:root{
  --brand-red:#7e1f24;
  --brand-blue:#4444aa;
  --text:#333;
  --page-bg:#eeeeee;
  --card-bg:#ffffff;
  --footer-bg:#3d3b3b;
  --footer-text:#e8e8e8;
}
*{box-sizing:border-box;margin:0;padding:0}
html,body{width:1200px;height:953px;overflow:hidden}
body{position:relative;background:var(--page-bg);font-family:"Source Sans 3",sans-serif;color:var(--text);font-size:13.5px}
.site-header{position:absolute;left:0;top:0;width:1200px;height:126px;background:#fff}
.brand{position:absolute;left:75px;top:48px;font-size:29px;color:var(--brand-red);font-family:"Source Sans 3",sans-serif;display:flex;align-items:center;gap:8px}
.brand-dot{width:10px;height:10px;border-radius:50%;background:var(--brand-blue)}
.logout{position:absolute;left:1045px;top:22px;width:80px;height:28px;background:var(--brand-red);color:#fff;border:none;font:14px "Source Sans 3",sans-serif;border-radius:2px}
.nav{position:absolute;right:74px;list-style:none;display:flex;gap:0;font-size:14px}
.nav li{margin-left:22px}
.nav-row-1{top:66px}
.nav-row-2{top:90px}
.nav .active{color:var(--brand-blue);position:relative}
.nav .active::after{content:"";position:absolute;left:-7px;right:-7px;top:22px;height:3px;background:var(--brand-blue)}
.nav .active::before{content:"";position:absolute;left:50%;top:24px;margin-left:-5px;border:5px solid transparent;border-top-color:var(--brand-blue)}
.clinic-title{position:absolute;left:0;width:1200px;top:186px;text-align:center;font:700 32px "Arimo",sans-serif;color:var(--brand-blue)}
.welcome{position:absolute;left:0;width:1200px;top:239px;text-align:center;font-size:21px;color:#333}
.prompt{position:absolute;left:75px;top:292px;font-size:21px;color:var(--brand-red)}
.card{position:absolute;background:var(--card-bg);box-shadow:0 3px 6px rgba(0,0,0,.08);padding:20px 20px}
.card h2{font:700 21px "Arimo",sans-serif;color:var(--brand-blue);margin-bottom:14px}
.card ul{list-style:none}
.card li{line-height:1.45;margin-bottom:9px;padding-left:12px;position:relative}
.card li::before{content:"•";position:absolute;left:0;color:var(--brand-blue)}
.card p{line-height:1.6;margin-bottom:12px}
.card-setup{left:76px;top:330px;width:324px;height:291px}
.card-schedule{left:437px;top:330px;width:324px;height:291px}
.card-campaigns{left:799px;top:330px;width:324px;height:291px}
.card-outbox{left:77px;top:659px;width:503px;height:129px}
.card-reviews{left:620px;top:659px;width:503px;height:129px}
.card-schedule li,.card-campaigns li{margin-bottom:6px}
.card-outbox li{margin-bottom:10px}
.reviews-links{display:flex;gap:34px;padding-left:12px}
.reviews-links a{color:var(--brand-blue);text-decoration:none}
.reviews-links span+a{margin-left:0}
.site-footer{position:absolute;left:0;top:851px;width:1200px;height:102px;background:var(--footer-bg);color:var(--footer-text);font-size:13.5px}
.login-info{position:absolute;left:77px;top:28px;line-height:2.1}
.copyright{position:absolute;right:77px;top:48px}
.page-count{position:absolute;right:16px;top:76px;font-size:12px}
</style>
</head>
<body>
<header class="site-header">
  <div class="brand"><span>BookWell</span><span class="brand-dot"></span></div>
  <button class="logout">Logout</button>
  <ul class="nav nav-row-1">
    <li class="active">Home</li><li>Schedule</li><li>Reviews</li><li>Clients</li><li>Campaigns</li><li>Marketing campaigns</li><li>Call out</li><li>Referrals</li><li>Outbox</li><li>Setup</li>
  </ul>
  <ul class="nav nav-row-2">
    <li>Synchronization alerts</li><li>Communications usage</li><li style="margin-left:32px">Users</li><li style="margin-left:27px">Reports</li>
  </ul>
</header>

<h1 class="clinic-title">The Veterinary Demo Clinic #2588</h1>
<p class="welcome">Welcome to your Liaison account</p>
<p class="prompt">What Do You Want To Do?</p>

<section class="card card-setup">
  <h2>Setup</h2>
  <ul>
    <li>Account information</li><li>Office hours</li><li>Online scheduling parameters</li><li>Client communications</li><li>Email templates</li><li>Online Scheduling website layout</li><li>Health certificates</li>
  </ul>
  <p style="margin-top:-8px">and more...</p>
</section>

<section class="card card-schedule">
  <h2>Schedule</h2>
  <p>View your appointment calendar by column or by provider</p>
  <p style="margin:20px 0 6px">Clients</p>
  <ul>
    <li>View client and patient records</li><li>View opt-out reports</li><li>View client appointment &amp; communication history</li>
  </ul>
</section>

<section class="card card-campaigns">
  <h2>Campaigns</h2>
  <p style="margin:20px 0 24px">Use the Media Center to:</p>
  <ul>
    <li>Send vaccine reminders through email, text, phone, or postcard</li><li>Send marketing communications</li>
  </ul>
</section>

<section class="card card-outbox">
  <h2>Outbox</h2>
  <ul>
    <li>View the account's communication history</li><li>Access the archives for any messages previously sent</li>
  </ul>
</section>

<section class="card card-reviews">
  <h2>Reviews</h2>
  <ul><li>View Surveys results and monitor any recent Surveys activity</li></ul>
  <div class="reviews-links"><span>Today is 4/4/2015</span><a href="#">Confirmation list</a><a href="#" style="margin-left:-12px">Task List</a></div>
</section>

<footer class="site-footer">
  <div class="login-info">Your are logged in as<br>a8Wk8ND &nbsp;(Administrator)</div>
  <div class="copyright">© 2014-2015, PetLedger-BookWell All rights reserved</div>
  <div class="page-count">x 6</div>
</footer>
</body>
</html>
```